Premium Juice and Wine Bottle Label

We require a premium label design for a Burgundy style wine bottle - the design should reflect pure and organic theme, with a reference to New Zealand blueberries. The winning design will look high-end, simple but sophisticated. Our logo is attached, refer :

https://www.rvcellar.co.nz and https://www.halopu.co.nz/wines/details/coming-soon-showcase/2018

for inspiration.

Target Market(s)

High-end retail grocery stores, wine shops, bars.

Requirements
Must have
• Label should leave enough space for barcode and nutrients/ingredients etc. Reference to New Zealand, natural-beverage, be very high-end in design. Refer links in project description for inspiration. Refer to attached logo, which must be used - feel free to change colour in order to obtain the best high-class design.
Nice to have
• N/A.
Should not have
• Cartoons or pictures of berries.

```html
<!DOCTYPE html>
<html lang="en">
<head>
<meta charset="utf-8">
<title>Marlow Lane – Wine Label</title>
<link rel="stylesheet" href="https://fonts.googleapis.com/css2?family=Cormorant+Garamond:wght@600&display=swap">
<style>
  :root {
    --page: #ffffff;
    --label-cream: #f3f1e3;
    --frame-light: #7b7bb3;
    --frame-dark: #24276f;
    --banner-light: #6c6aa8;
    --banner-dark: #1b1f6e;
    --band-gold: #a59130;
    --band-line: #f3f1e3;
    --berry-light: #5a6fb5;
    --berry-dark: #2b3575;
    --ink-navy: #1f2474;
    --logo-white: #ffffff;
  }
  html, body {
    margin: 0;
    padding: 0;
    width: 1200px;
    height: 1194px;
    overflow: hidden;
    background: var(--page);
  }
  .canvas {
    position: relative;
    width: 1200px;
    height: 1194px;
  }
  .wine-label {
    position: absolute;
    left: 200px;
    top: 211px;
    width: 800px;
    height: 772px;
    background: var(--label-cream);
    box-sizing: border-box;
    border: 5px solid var(--frame-light);
    border-image: linear-gradient(90deg, var(--frame-light), var(--frame-dark) 50%, var(--frame-light)) 1;
  }
  .brand-banner {
    position: absolute;
    left: 204px;
    top: -56px;
    width: 351px;
    height: 333px;
  }
  .brand-name {
    position: absolute;
    left: 204px;
    top: 40px;
    width: 351px;
    margin: 0;
    text-align: center;
    font-family: "Cormorant Garamond", serif;
    font-weight: 600;
    font-size: 74px;
    line-height: 0.95;
    color: var(--logo-white);
  }
  .fruit-band {
    position: absolute;
    left: 174px;
    top: 454px;
    width: 441px;
    height: 69px;
  }
  .berry-art {
    position: absolute;
    left: 312px;
    top: 409px;
    width: 213px;
    height: 160px;
    border-radius: 80px;
    background: radial-gradient(ellipse at 45% 40%, var(--berry-light), var(--berry-dark));
  }
  .origin {
    position: absolute;
    left: 0;
    width: 790px;
    top: 602px;
    margin: 0;
    text-align: center;
    font-family: "Cormorant Garamond", serif;
    font-weight: 600;
    font-size: 40px;
    letter-spacing: 1px;
    color: var(--ink-navy);
  }
</style>
</head>
<body>
<main class="canvas">
  <section class="wine-label">
    <svg class="brand-banner" viewBox="0 0 351 333" aria-hidden="true">
      <defs>
        <linearGradient id="bannerFill" x1="0" x2="1" y1="0" y2="0">
          <stop offset="0" stop-color="#6c6aa8"/>
          <stop offset="0.55" stop-color="#1b1f6e"/>
          <stop offset="1" stop-color="#56569a"/>
        </linearGradient>
      </defs>
      <polygon points="0,0 351,0 351,277 175.5,333 0,277" fill="url(#bannerFill)"/>
    </svg>
    <h1 class="brand-name">Marlow<br>Lane</h1>

    <svg class="fruit-band" viewBox="0 0 441 69" aria-hidden="true">
      <rect x="0" y="4" width="441" height="61" fill="#a59130"/>
      <rect x="0" y="25" width="441" height="3" fill="#f3f1e3"/>
      <rect x="0" y="41" width="441" height="3" fill="#f3f1e3"/>
    </svg>
    <div class="berry-art" role="img" aria-label="Illustration of a small cluster of New Zealand blueberries"></div>

    <p class="origin">NEW ZEALAND</p>
  </section>
</main>
</body>
</html>
```